Acupuncture Medspa needs a business card design

I need a business card design that looks professional, has a spa-like quality and can offer a promo on the back. Initial promo is "First session free". The tagline of NeedleNook is: Refresh, Restore, Rejuvenate.

NeedleNook is a membership-based acupuncture medspa that offers acupuncture, cupping, and herbal therapies. Members choose between the "Refresh" membership which is for stress relief, or "Restore" which is for treating health conditions, and lastly "Rejuvenate" which is for natural facial enhancement.

Industry/Entity Type

Health And Wellness

Contact Information for Business Card

Coral Haskins, MAC, L.Ac.
612-555-0193
www.needlenook-example.com

Font styles to use
Serif
Sans Serif

Colors

Designer to choose colors to be used in the design.

Requirements
Must have
• The project must have NeedleNook logo, promo on the back, and contact information
Nice to have
• I would like to see the colors of the logo used.

```html
<!DOCTYPE html>
<html lang="en">
<head>
<meta charset="utf-8">
<title>NeedleNook Business Card</title>
<link rel="stylesheet" href="https://fonts.googleapis.com/css2?family=Montserrat:wght@300;400;500;600&display=swap">
<style>
  :root {
    --teal: #218f89;
    --teal-deep: #158a83;
    --teal-faint: rgba(255, 255, 255, 0.07);
    --white: #ffffff;
    --muted-white: rgba(255, 255, 255, 0.72);
    --ink-brown: #3a2a22;
    --backdrop: #ece7e1;
  }
  * { margin: 0; padding: 0; box-sizing: border-box; }
  html, body {
    width: 1200px;
    height: 960px;
    overflow: hidden;
    background: var(--backdrop);
    font-family: "Montserrat", sans-serif;
  }
  .canvas {
    position: relative;
    width: 1200px;
    height: 960px;
  }
  .card {
    position: absolute;
    left: 220px;
    width: 760px;
    height: 380px;
    overflow: hidden;
    box-shadow: 0 10px 28px rgba(60, 45, 30, 0.25);
  }
  /* Front */
  .card-front {
    top: 70px;
    background: var(--teal);
    display: flex;
    align-items: center;
    justify-content: center;
  }
  .front-decor {
    position: absolute;
    left: 50%;
    top: 50%;
    width: 330px;
    height: 330px;
    margin: -150px 0 0 -165px;
    border-radius: 50%;
    border: 6px solid var(--teal-faint);
  }
  .wordmark {
    position: relative;
    color: var(--white);
    font-weight: 600;
    font-size: 58px;
    letter-spacing: 3px;
    text-transform: uppercase;
  }
  /* Back */
  .card-back {
    top: 510px;
    background: var(--white);
    display: flex;
  }
  .back-panel {
    position: relative;
    width: 280px;
    background: var(--teal-deep);
    color: var(--white);
  }
  .person-name {
    position: absolute;
    right: 18px;
    top: 100px;
    font-size: 25px;
    font-weight: 400;
    text-transform: uppercase;
    text-align: right;
  }
  .person-credentials {
    position: absolute;
    right: 18px;
    top: 140px;
    font-size: 17px;
    font-weight: 300;
    color: var(--muted-white);
    text-transform: uppercase;
  }
  .panel-mark {
    position: absolute;
    left: 50%;
    bottom: 40px;
    width: 150px;
    height: 150px;
    margin-left: -75px;
    border-radius: 50%;
    border: 2px solid rgba(255, 255, 255, 0.45);
  }
  .back-main {
    position: relative;
    flex: 1;
  }
  .promo {
    position: absolute;
    right: 50px;
    top: 30px;
    width: 160px;
    height: 160px;
    border-radius: 50%;
    border: 2px solid var(--teal);
    display: flex;
    flex-direction: column;
    align-items: center;
    justify-content: center;
    color: var(--teal);
    text-transform: uppercase;
    text-align: center;
  }
  .promo-first {
    font-size: 24px;
    font-weight: 600;
    letter-spacing: 5px;
  }
  .promo-number {
    font-size: 40px;
    font-weight: 300;
    color: var(--ink-brown);
    line-height: 1.1;
  }
  .promo-rest {
    font-size: 13px;
    font-weight: 400;
    letter-spacing: 3px;
  }
  .contact {
    position: absolute;
    right: 44px;
    top: 245px;
    text-align: right;
    color: var(--teal);
  }
  .contact-phone {
    font-size: 34px;
    font-weight: 400;
    letter-spacing: 2px;
  }
  .contact-web {
    margin-top: 6px;
    font-size: 14px;
    font-weight: 400;
    letter-spacing: 1.5px;
    text-transform: uppercase;
  }
</style>
</head>
<body>
<main class="canvas">
  <section class="card card-front" aria-label="Card front">
    <div class="front-decor"></div>
    <h1 class="wordmark">NeedleNook</h1>
  </section>

  <section class="card card-back" aria-label="Card back">
    <div class="back-panel">
      <p class="person-name">Coral Haskins,</p>
      <p class="person-credentials">MAC, L.Ac.</p>
      <div class="panel-mark"></div>
    </div>
    <div class="back-main">
      <div class="promo">
        <span class="promo-first">First</span>
        <span class="promo-number">1</span>
        <span class="promo-rest">Free Session</span>
      </div>
      <div class="contact">
        <p class="contact-phone">612-555-0193</p>
        <p class="contact-web">www.needlenook-example.com</p>
      </div>
    </div>
  </section>
</main>
</body>
</html>
```